Premium Juice and Wine Bottle Label

We require a premium label design for a Burgundy style wine bottle - the design should reflect pure and organic theme, with a reference to New Zealand blueberries. The winning design will look high-end, simple but sophisticated. Our logo is attached, refer :

https://www.orvalecellars.co.nz and https://www.pirovane.co.nz/wines/details/coming-soon-showcase/2018

for inspiration.

Target Market(s)

High-end retail grocery stores, wine shops, bars.

Requirements
Must have
• Label should leave enough space for barcode and nutrients/ingredients etc. Reference to New Zealand, natural-beverage, be very high-end in design. Refer links in project description for inspiration. Refer to attached logo, which must be used - feel free to change colour in order to obtain the best high-class design.
Nice to have
• N/A.
Should not have
• Cartoons or pictures of berries.

```html
<!DOCTYPE html>
<html lang="en">
<head>
<meta charset="utf-8">
<title>Kerrow Lane – Label Range</title>
<link rel="stylesheet" href="https://fonts.googleapis.com/css2?family=Poiret+One&display=swap">
<style>
  :root {
    --white: #ffffff;
    --teal-bg: #123a40;
    --teal-banner: #0e2a2e;
    --teal-label: #1c4b53;
    --teal-ribbon: #143a40;
    --teal-accent: #5cc4cc;
    --purple-bg: #6c1d82;
    --purple-banner: #2a0b35;
    --purple-label: #6a1f80;
    --purple-ribbon: #8a2fa3;
    --purple-art: #5a1670;
    --tan-bg: #b29e7a;
    --tan-banner: #706449;
    --tan-label: #ddd0ae;
    --tan-ribbon: #cdbf98;
    --tan-art: #f2ece0;
    --red-bg: #830008;
    --red-banner: #b8001a;
    --red-label: #f6f6f6;
    --red-ribbon: #d00a24;
    --red-art: #f1c9ce;
    --type: "Poiret One", sans-serif;
  }
  * { box-sizing: border-box; margin: 0; padding: 0; }
  html, body { width: 1200px; height: 807px; overflow: hidden; }
  body { position: relative; font-family: var(--type); background: var(--teal-bg); }

  .panel { position: absolute; overflow: hidden; }
  .panel--blueberry { left: 0; top: 0; width: 606px; height: 403px; background: radial-gradient(circle at 48% 45%, #1a4c54, var(--teal-bg) 70%); }
  .panel--grape { left: 606px; top: 0; width: 594px; height: 403px; background: radial-gradient(circle at 48% 45%, #7b2393, var(--purple-bg) 70%); }
  .panel--cream { left: 0; top: 403px; width: 597px; height: 404px; background: radial-gradient(circle at 48% 45%, #c5b28e, var(--tan-bg) 70%); }
  .panel--cherry { left: 597px; top: 403px; width: 603px; height: 404px; background: radial-gradient(circle at 48% 45%, #9c0010, var(--red-bg) 70%); }

  .brand-banner {
    position: absolute; top: 0; left: 456px; width: 120px; height: 128px;
    clip-path: polygon(0 0, 100% 0, 100% 86%, 50% 100%, 0 86%);
  }
  .panel--cream .brand-banner { left: 448px; }
  .panel--blueberry .brand-banner { background: var(--teal-banner); }
  .panel--grape .brand-banner { background: var(--purple-banner); }
  .panel--cream .brand-banner { background: var(--tan-banner); }
  .panel--cherry .brand-banner { background: var(--red-banner); }

  .brand-name {
    position: absolute; top: 26px; left: 438px;
    color: var(--white); font-size: 40px; line-height: 40px; letter-spacing: 1px;
  }
  .brand-name span { display: block; }
  .brand-name span + span { padding-left: 44px; }
  .panel--cream .brand-name { left: 432px; }

  .label {
    position: absolute; left: 266px; top: 166px; width: 89px; height: 232px;
    display: flex; flex-direction: column; align-items: center;
  }
  .panel--cream .label { left: 260px; top: 171px; height: 226px; }
  .panel--cherry .label { left: 268px; top: 178px; width: 87px; height: 212px; }
  .panel--blueberry .label { background: var(--teal-label); }
  .panel--grape .label { background: var(--purple-label); }
  .panel--cream .label { background: var(--tan-label); }
  .panel--cherry .label { background: var(--red-label); }

  .label__ribbon {
    width: 66px; height: 88px; flex: none;
    clip-path: polygon(0 0, 100% 0, 100% 84%, 50% 100%, 0 84%);
    display: flex; flex-direction: column; justify-content: center;
    color: var(--white); font-size: 16px; line-height: 16px; text-align: center;
  }
  .label__ribbon span + span { padding-left: 14px; }
  .panel--blueberry .label__ribbon { background: var(--teal-ribbon); }
  .panel--grape .label__ribbon { background: var(--purple-ribbon); }
  .panel--cream .label__ribbon { background: var(--tan-ribbon); }
  .panel--cherry .label__ribbon { background: var(--red-ribbon); }

  .label__art { width: 66px; height: 80px; margin-top: 10px; border-radius: 4px; flex: none; }
  .panel--blueberry .label__art { background: radial-gradient(circle, #3d7078, var(--teal-label)); }
  .panel--grape .label__art { background: radial-gradient(circle, #8c3ea3, var(--purple-art)); }
  .panel--cream .label__art { width: 87px; height: 36px; margin-top: 18px; border-radius: 0; background: linear-gradient(180deg, var(--tan-label), var(--tan-art) 50%, var(--tan-label)); }
  .panel--cherry .label__art { height: 84px; margin-top: 6px; background: radial-gradient(circle, var(--red-art), var(--red-label) 75%); }

  .label__title { margin-top: auto; margin-bottom: 8px; text-align: center; color: var(--white); }
  .label__origin { font-size: 12px; line-height: 13px; letter-spacing: 0.5px; }
  .label__fruit { font-size: 12.5px; line-height: 14px; color: var(--teal-accent); letter-spacing: 0.5px; }
  .panel--grape .label__title { font-size: 22px; line-height: 24px; margin-bottom: 12px; }
  .panel--cream .label__title { font-size: 31px; line-height: 31px; margin-bottom: 6px; color: #f4efe2; }
  .panel--cherry .label__title { font-size: 22px; line-height: 24px; margin-bottom: 6px; color: var(--red-ribbon); }
</style>
</head>
<body>
  <section class="panel panel--blueberry">
    <div class="brand-banner"></div>
    <div class="brand-name"><span>Kerrow</span><span>Lane</span></div>
    <article class="label">
      <div class="label__ribbon"><span>Kerrow</span><span>Lane</span></div>
      <div class="label__art" role="img" aria-label="Line illustration of a blueberry sprig"></div>
      <div class="label__title">
        <div class="label__origin">NEW ZEALAND</div>
        <div class="label__fruit">BLUEBERRIES</div>
      </div>
    </article>
  </section>

  <section class="panel panel--grape">
    <div class="brand-banner"></div>
    <div class="brand-name"><span>Kerrow</span><span>Lane</span></div>
    <article class="label">
      <div class="label__ribbon"><span>Kerrow</span><span>Lane</span></div>
      <div class="label__art" role="img" aria-label="Line illustration of a bunch of grapes"></div>
      <div class="label__title">GRAPES</div>
    </article>
  </section>

  <section class="panel panel--cream">
    <div class="brand-banner"></div>
    <div class="brand-name"><span>Kerrow</span><span>Lane</span></div>
    <article class="label">
      <div class="label__ribbon"><span>Kerrow</span><span>Lane</span></div>
      <div class="label__art" role="img" aria-label="Crossed white ribbon decoration"></div>
      <div class="label__title">IRISH<br>CREAM</div>
    </article>
  </section>

  <section class="panel panel--cherry">
    <div class="brand-banner"></div>
    <div class="brand-name"><span>Kerrow</span><span>Lane</span></div>
    <article class="label">
      <div class="label__ribbon"><span>Kerrow</span><span>Lane</span></div>
      <div class="label__art" role="img" aria-label="Line illustration of a pair of cherries"></div>
      <div class="label__title">CHERRY</div>
    </article>
  </section>
</body>
</html>
```